Professional business cards for our auto wholesale dealership.

Target Market(s)

New and used cars sales managers and middle class to higher end private party buyers.

Industry/Entity Type

Automotive

Contact Information for Business Card

Bayline Premier Motors
Marcus T Holloway
Owner
(555) 417-3860
baypremmotors@mailbox-example.net
Dealer Lic # 48261

Logo Text

Bayline Premier Motors, Bay Prem Motors, BPM, etc

Font styles to use
Serif
Sans Serif

Colors

Designer to choose colors to be used in the design.

Requirements
Must have
• A professional, but not pretentious, look
Nice to have
• It might be nice to see "BPM" in a shape form i.e. circle, triangle, etc in the corner or background somehwere
Should not have
• bright "girly" colors

```html
<!DOCTYPE html>
<html lang="en">
<head>
<meta charset="utf-8">
<title>Bayline Premier Motors — Business Card</title>
<link rel="stylesheet" href="https://fonts.googleapis.com/css2?family=Open+Sans:wght@400;600;700&display=swap">
<style>
  :root {
    --page-bg: #d2d0d1;
    --card-black: #141414;
    --card-black-deep: #070707;
    --card-white: #ffffff;
    --brand-red: #c4161c;
    --brand-red-dark: #7d0c10;
    --text-light: #f2f2f2;
    --shadow: rgba(0, 0, 0, 0.28);
  }
  * { box-sizing: border-box; margin: 0; padding: 0; }
  html, body {
    width: 1200px;
    height: 900px;
    overflow: hidden;
    background: var(--page-bg);
    font-family: "Open Sans", Arial, sans-serif;
  }
  .canvas {
    position: relative;
    width: 1200px;
    height: 900px;
  }
  .card {
    position: absolute;
    top: 295px;
    width: 540px;
    height: 310px;
    border-radius: 22px;
    overflow: hidden;
    box-shadow: 0 14px 30px var(--shadow);
  }
  .card--front { left: 40px; }
  .card--back { left: 620px; }
  .card__art {
    position: absolute;
    inset: 0;
    width: 100%;
    height: 100%;
  }

  /* Front: brand block on white panel */
  .front-brand {
    position: absolute;
    left: 24px;
    top: 88px;
    width: 190px;
    text-align: center;
  }
  .brand-dot {
    display: block;
    width: 34px;
    height: 34px;
    margin: 0 auto 12px;
    border-radius: 50%;
    background: var(--brand-red);
  }
  .front-brand__name {
    color: var(--brand-red);
    font-weight: 700;
    font-size: 22px;
    line-height: 1.15;
    text-transform: uppercase;
  }

  /* Front: contact block */
  .contact {
    position: absolute;
    left: 262px;
    top: 98px;
    width: 266px;
    text-align: center;
    color: var(--text-light);
  }
  .contact__name {
    color: var(--brand-red);
    font-weight: 600;
    font-size: 19px;
    line-height: 1.2;
  }
  .contact__role {
    font-size: 13px;
    margin-top: 3px;
  }
  .contact__phone {
    font-weight: 600;
    font-size: 19px;
    margin-top: 26px;
  }
  .contact__line {
    font-size: 13px;
    line-height: 1.4;
  }
  .contact__email { margin-top: 4px; }

  /* Back: centred brand */
  .back-brand {
    position: absolute;
    left: 0;
    right: 0;
    top: 92px;
    text-align: center;
  }
  .back-brand .brand-dot {
    width: 56px;
    height: 56px;
    margin-bottom: 22px;
  }
  .back-brand__name {
    color: var(--brand-red);
    font-weight: 700;
    font-size: 26px;
    letter-spacing: 3px;
    text-transform: uppercase;
  }
</style>
</head>
<body>
<main class="canvas">

  <section class="card card--front" aria-label="Business card front">
    <svg class="card__art" viewBox="0 0 540 310" aria-hidden="true">
      <defs>
        <linearGradient id="front-black" x1="0" y1="0" x2="1" y2="1">
          <stop offset="0" stop-color="#1d1d1d"/>
          <stop offset="1" stop-color="#060606"/>
        </linearGradient>
        <linearGradient id="front-swoosh" x1="0" y1="0" x2="0" y2="1">
          <stop offset="0" stop-color="#e02027"/>
          <stop offset="0.6" stop-color="#9c1015"/>
          <stop offset="1" stop-color="#5e090c"/>
        </linearGradient>
      </defs>
      <rect width="540" height="310" fill="url(#front-black)"/>
      <path d="M0,0 H266 C324,92 292,242 200,310 H0 Z" fill="url(#front-swoosh)"/>
      <path d="M0,0 H236 C300,88 282,236 188,310 H0 Z" fill="#ffffff"/>
    </svg>

    <div class="front-brand">
      <span class="brand-dot"></span>
      <p class="front-brand__name">Bayline Premier Motors</p>
    </div>

    <div class="contact">
      <p class="contact__name">Marcus T Holloway</p>
      <p class="contact__role">Owner</p>
      <p class="contact__phone">(555) 417-3860</p>
      <p class="contact__line contact__email">baypremmotors@mailbox-example.net</p>
      <p class="contact__line">Dealer Lic # 48261</p>
    </div>
  </section>

  <section class="card card--back" aria-label="Business card back">
    <svg class="card__art" viewBox="0 0 540 310" aria-hidden="true">
      <defs>
        <radialGradient id="back-black" cx="0.5" cy="0.45" r="0.7">
          <stop offset="0" stop-color="#1e1e1e"/>
          <stop offset="1" stop-color="#070707"/>
        </radialGradient>
      </defs>
      <rect width="540" height="310" fill="url(#back-black)"/>
      <circle cx="270" cy="150" r="128" fill="none" stroke="#2a1213" stroke-width="26"/>
    </svg>

    <div class="back-brand">
      <span class="brand-dot"></span>
      <p class="back-brand__name">Bayline Premier Motors</p>
    </div>
  </section>

</main>
</body>
</html>
```